Professional business cards for real estate development company

I need business cards for my new real estate development company. The company, "KORVA" is a real estate development, investment, and advisory firm with a focus on multifamily, office, and mixed-use projects across primary and secondary markets in the Southeast United States.

Style preference is modern

Industry/Entity Type

Real Estate Development

Contact Information for Business Card

The business cards need to include:
Name
Title
Mailing Address
Phone Number
Web Address

Logo is attached. I would like white to be the primary color with incorporation of the company colors: #232D3A and #B5A451

Font styles to use
Other font styles liked:
• Montserrat, Avenir

Requirements
Must have
• Company Logo. No need to include the company name since the name is in the logo.
Should not have
• No line type designs

```html
<!DOCTYPE html>
<html lang="en">
<head>
<meta charset="utf-8">
<title>KORVA Business Card</title>
<link href="https://fonts.googleapis.com/css2?family=Roboto:wght@400;500;700&display=swap" rel="stylesheet">
<style>
  :root {
    --navy: #232D3A;
    --gold: #B5A451;
    --white: #FFFFFF;
    --backdrop: #DDDEDF;
    --ink: #1E2530;
  }
  * { margin: 0; padding: 0; box-sizing: border-box; }
  html, body {
    width: 1200px;
    height: 900px;
    overflow: hidden;
    background: var(--backdrop);
    font-family: "Roboto", Arial, sans-serif;
  }
  .canvas { position: relative; width: 1200px; height: 900px; }

  .card { position: absolute; top: 216px; width: 309px; height: 501px; }

  .card-front {
    left: 279px;
    background: var(--navy);
    border-radius: 0 62px 0 62px;
    display: flex;
    align-items: center;
    justify-content: center;
  }
  .card-back {
    left: 617px;
    background: var(--white);
    border-radius: 62px 0 62px 0;
  }

  .wordmark {
    font-weight: 500;
    font-size: 50px;
    letter-spacing: 4px;
    line-height: 1;
  }
  .card-front .wordmark { color: var(--gold); margin-top: 18px; }
  .card-back .wordmark {
    position: absolute;
    top: 150px;
    left: 0;
    width: 100%;
    text-align: center;
    color: var(--navy);
  }

  .contact-block {
    position: absolute;
    left: 37px;
    top: 293px;
    color: var(--ink);
  }
  .person-name {
    font-weight: 700;
    font-size: 19.5px;
    color: var(--navy);
    line-height: 1.05;
  }
  .person-title { font-size: 14.5px; line-height: 1.2; }

  .contact-list { list-style: none; margin-top: 14px; }
  .contact-list li {
    display: flex;
    align-items: center;
    font-size: 14.2px;
    height: 19px;
  }
  .contact-list svg { width: 15px; height: 15px; margin-right: 5px; flex: none; fill: var(--navy); }

  .address {
    display: flex;
    margin-top: 17px;
    font-size: 14.2px;
    line-height: 18px;
  }
  .address svg { width: 12px; height: 16px; margin: 1px 5px 0 2px; flex: none; fill: var(--navy); }
</style>
</head>
<body>
<main class="canvas">
  <section class="card card-front">
    <div class="wordmark">KORVA</div>
  </section>

  <section class="card card-back">
    <div class="wordmark">KORVA</div>

    <div class="contact-block">
      <h1 class="person-name">DANIEL HARPER</h1>
      <p class="person-title">Managing Director</p>

      <ul class="contact-list">
        <li>
          <svg viewBox="0 0 24 24" aria-hidden="true"><path d="M6.6 10.8c1.4 2.8 3.8 5.1 6.6 6.6l2.2-2.2c.3-.3.7-.4 1-.2 1.1.4 2.3.6 3.6.6.6 0 1 .4 1 1V20c0 .6-.4 1-1 1C10.6 21 3 13.4 3 4c0-.6.4-1 1-1h3.5c.6 0 1 .4 1 1 0 1.3.2 2.5.6 3.6.1.3 0 .7-.2 1L6.6 10.8z"/></svg>
          044-321 654 987
        </li>
        <li>
          <svg viewBox="0 0 24 24" aria-hidden="true"><path d="M2 5h20v14H2z M4 7l8 6 8-6" fill="none" stroke="#232D3A" stroke-width="2"/><path d="M2 5h20v3l-10 7L2 8z"/></svg>
          hello@korvamail.com
        </li>
        <li>
          <svg viewBox="0 0 24 24" aria-hidden="true"><g fill="none" stroke="#232D3A" stroke-width="1.8"><circle cx="12" cy="12" r="9.5"/><ellipse cx="12" cy="12" rx="4.2" ry="9.5"/><path d="M2.5 12h19M4 7h16M4 17h16"/></g></svg>
          www.korvasite.com
        </li>
      </ul>

      <div class="address">
        <svg viewBox="0 0 12 16" aria-hidden="true"><path d="M6 0C2.7 0 0 2.6 0 5.9 0 10 6 16 6 16s6-6 6-10.1C12 2.6 9.3 0 6 0zm0 8.2a2.4 2.4 0 110-4.8 2.4 2.4 0 010 4.8z"/></svg>
        <p>318, Harbor Street<br>Stateland, 30981</p>
      </div>
    </div>
  </section>
</main>
</body>
</html>
```